Strategic design partner needed for newly global technical consultancy! Starting with PowerPoint!

Veltrano.biz is a new consulting company offering technical assurance (reliability, business and cyber resiliency, operational excellence, and technical agility). We already have a logo (attached) and main font (Montserrat). Our colour scheme is gold and charcoal (color code of charcoal is #36454F, and for the gold is #B69904).
See the attachment for full colour palette we want! We need to partner with a designer for our corporate branding, starting with a PowerPoint deck that will be used for proposals and client meetings.
In a proposal deck we have items like Problem Statement (our joint understanding), Our Approach, Architecture, Timeline, Team, Assumptions/Dependencies/Risks, RACI, Pricing.
For corporate presentations we would have Introduction, Services, Methodology, Case Studies, Team, Clients, Contact.
This could lead to much more work. The website is just a placeholder, but we like the colours (veltrano dot biz)

Industry/Entity Type

Technology solutions apply across all industries. We have clients in fintech, pharma, retail, etc.

Requirements
Must have
• Match the colour scheme - SEE UPLOADED ATTACHMENT

```html
<!DOCTYPE html>
<html lang="en">
<head>
<meta charset="utf-8">
<title>Veltrano.biz – Corporate Deck Overview</title>
<link href="https://fonts.googleapis.com/css2?family=Montserrat:ital,wght@0,400;0,600;0,700;1,400&display=swap" rel="stylesheet">
<style>
  :root{
    --canvas:#c9cacc;
    --gold:#c9962e;
    --charcoal:#36454f;
    --grey:#8a8a8a;
    --light:#eeeeee;
    --ink:#4a4a4a;
    --white:#ffffff;
  }
  *{margin:0;padding:0;box-sizing:border-box}
  html,body{width:1200px;height:850px;overflow:hidden}
  body{background:var(--canvas);font-family:"Montserrat",sans-serif;position:relative}
  .slide{position:absolute;width:176px;height:99px;background:var(--white);box-shadow:0 2px 4px rgba(0,0,0,.18);overflow:hidden}
  .slide svg{display:block;width:176px;height:99px}
  .gold{fill:var(--gold)} .char{fill:var(--charcoal)} .grey{fill:var(--grey)} .light{fill:var(--light)} .wht{fill:var(--white)}
  .sg{stroke:var(--gold)} .sc{stroke:var(--charcoal)} .sl{stroke:#cfcfcf}
  text{font-family:"Montserrat",sans-serif}
  .h{fill:var(--gold);font-weight:700;font-size:4.4px}
  .hc{text-anchor:middle}
  .b{fill:var(--ink);font-size:1.9px}
  .bw{fill:var(--white);font-size:1.9px}
  .s{fill:var(--ink);font-size:2.4px;font-weight:600}
  .sgd{fill:var(--gold);font-size:2.4px;font-weight:700}
  .num{fill:var(--gold);font-weight:700;font-size:3.2px}
  .pg{fill:var(--white);font-size:1.6px;text-anchor:end}
  .photo-warm{fill:url(#warm)} .photo-cool{fill:url(#cool)}
</style>
</head>
<body>
<svg width="0" height="0" style="position:absolute">
  <defs>
    <linearGradient id="warm" x1="0" y1="0" x2="1" y2="1"><stop offset="0" stop-color="#6f5a45"/><stop offset="1" stop-color="#b79b74"/></linearGradient>
    <linearGradient id="cool" x1="0" y1="0" x2="1" y2="1"><stop offset="0" stop-color="#3f4d5c"/><stop offset="1" stop-color="#9aa7b3"/></linearGradient>
  </defs>
</svg>

<!-- Row 1 -->
<div class="slide cover" style="left:54px;top:57px">
  <svg viewBox="0 0 176 99">
    <rect role="img" aria-label="Photo of a businessman holding a tablet" class="photo-cool" width="176" height="45"/>
    <rect class="gold" y="45" width="176" height="54"/>
    <text x="9" y="58" fill="#fff" font-size="6">PRESENTATION TITLE</text>
    <text x="9" y="66" fill="#fff" font-size="4.2" font-weight="700">SUBTITLE</text>
    <circle cx="144" cy="55" r="3" fill="none" stroke="#36454f" stroke-width=".8"/>
    <text x="144" y="66" class="hc" fill="#36454f" font-size="5.6" font-weight="600">Veltrano.biz</text>
    <text x="9" y="93" fill="#fff" font-size="2.2">JANUARY 2025</text>
    <text x="167" y="93" fill="#fff" font-size="2.2" text-anchor="end">VELTRANO.BIZ</text>
  </svg>
</div>

<div class="slide contents" style="left:266px;top:57px">
  <svg viewBox="0 0 176 99">
    <text class="h hc" x="88" y="13">Contents</text>
    <g class="b">
      <text x="26" y="27">Cover Slide</text><text x="126" y="27" text-anchor="end">01</text>
      <text x="26" y="39">Contents</text><text x="126" y="39" text-anchor="end">03</text>
      <text x="26" y="52">About Us</text><text x="126" y="52" text-anchor="end">04</text>
      <text x="26" y="65">Our Mission</text><text x="126" y="65" text-anchor="end">05</text>
      <text x="26" y="79">Our Vision</text><text x="126" y="79" text-anchor="end">07</text>
      <text x="99" y="27">Infographic 1</text><text x="142" y="27" text-anchor="end">01</text>
      <text x="99" y="39">Planning</text><text x="142" y="39" text-anchor="end">03</text>
      <text x="99" y="52">Company info</text><text x="142" y="52" text-anchor="end">04</text>
      <text x="99" y="65">Our Team</text><text x="142" y="65" text-anchor="end">06</text>
      <text x="99" y="79">Dashboard</text><text x="142" y="79" text-anchor="end">07</text>
    </g>
    <g class="sl" stroke-width=".3">
      <line x1="26" y1="29" x2="67" y2="29"/><line x1="26" y1="41" x2="67" y2="41"/><line x1="26" y1="54" x2="67" y2="54"/><line x1="26" y1="67" x2="67" y2="67"/><line x1="26" y1="81" x2="67" y2="81"/>
      <line x1="99" y1="29" x2="142" y2="29"/><line x1="99" y1="41" x2="142" y2="41"/><line x1="99" y1="54" x2="142" y2="54"/><line x1="99" y1="67" x2="142" y2="67"/><line x1="99" y1="81" x2="142" y2="81"/>
    </g>
    <rect class="gold" y="92" width="176" height="7"/><circle cx="8" cy="95.5" r="1.4" fill="#fff" opacity=".7"/><text class="pg" x="167" y="96.3">PAGE | 02</text>
  </svg>
</div>

<div class="slide problem" style="left:490px;top:57px">
  <svg viewBox="0 0 176 99">
    <text class="h hc" x="88" y="13">Problem Statement</text>
    <rect class="char" x="9" y="27" width="167" height="31"/>
    <g fill="#fff" font-size="3.1" font-style="italic">
      <text x="18" y="34.5">We define the challenge together, map the risks and agree</text>
      <text x="18" y="41">on clear goals for reliability and resilience across every</text>
      <text x="18" y="47.5">system, so that each decision we take is grounded in data</text>
      <text x="18" y="54">and shared understanding with the client team involved.</text>
    </g>
    <rect class="gold" y="92" width="176" height="7"/><circle cx="8" cy="95.5" r="1.4" fill="#fff" opacity=".7"/><text class="pg" x="167" y="96.3">PAGE | 03</text>
  </svg>
</div>

<div class="slide mission" style="left:717px;top:57px">
  <svg viewBox="0 0 176 99">
    <text class="h hc" x="88" y="13">Our Mission</text>
    <rect class="light" x="12" y="28" width="43" height="22"/>
    <rect class="light" x="124" y="53" width="43" height="22"/>
    <g class="sgd" font-size="2.3" text-anchor="middle">
      <text x="34" y="36">Mission 1</text><text x="86" y="36">Mission 1</text><text x="145" y="36">Mission 1</text>
      <text x="34" y="61">Mission 1</text><text x="86" y="61">Mission 1</text><text x="145" y="61">Mission 1</text>
    </g>
    <g class="b" font-size="1.6" text-anchor="middle">
      <text x="34" y="39.5">Clear goals, steady delivery</text><text x="34" y="42">and lasting value for clients</text>
      <text x="86" y="39.5">Clear goals, steady delivery</text><text x="86" y="42">and lasting value for clients</text>
      <text x="145" y="39.5">Clear goals, steady delivery</text><text x="145" y="42">and lasting value for clients</text>
      <text x="34" y="64.5">Clear goals, steady delivery</text><text x="34" y="67">and lasting value for clients</text>
      <text x="86" y="64.5">Clear goals, steady delivery</text><text x="86" y="67">and lasting value for clients</text>
      <text x="145" y="64.5">Clear goals, steady delivery</text><text x="145" y="67">and lasting value for clients</text>
    </g>
    <rect class="gold" y="92" width="176" height="7"/><circle cx="8" cy="95.5" r="1.4" fill="#fff" opacity=".7"/><text class="pg" x="167" y="96.3">PAGE | 04</text>
  </svg>
</div>

<div class="slide achievements" style="left:933px;top:57px">
  <svg viewBox="0 0 176 99">
    <rect role="img" aria-label="Photo of two colleagues working at a laptop" class="photo-warm" width="67" height="92"/>
    <text class="h" x="73" y="28">Our Acheivements</text>
    <g class="b"><text x="73" y="34">We deliver measurable results for clients in many</text><text x="73" y="36.5">sectors, building trust through reliable systems and</text><text x="73" y="39">clear reporting at every stage of each engagement.</text></g>
    <rect class="light" x="73" y="49" width="26" height="12"/><rect class="light" x="100" y="49" width="26" height="12"/><rect class="char" x="127" y="49" width="26" height="12"/>
    <text class="num" x="75" y="54" font-size="2.4">15</text><text class="b" x="75" y="58.5" font-size="2.2">Companies</text>
    <text class="num" x="102" y="54" font-size="2.4">1,000</text><text class="b" x="102" y="58.5" font-size="2.2">Clients</text>
    <text x="129" y="54" fill="#fff" font-size="2.4" font-weight="700">46</text><text class="bw" x="129" y="58.5" font-size="2.2">Employees</text>
    <rect class="gold" y="92" width="176" height="7"/><text class="pg" x="167" y="96.3">PAGE | 05</text>
  </svg>
</div>

<!-- Row 2 -->
<div class="slide services" style="left:54px;top:190px">
  <svg viewBox="0 0 176 99">
    <text class="h hc" x="88" y="13">Services</text>
    <g class="b" text-anchor="middle"><text x="88" y="17">Technical assurance for reliable, resilient systems</text><text x="88" y="19.5">across every industry we serve worldwide.</text></g>
    <rect role="img" aria-label="Photo of hands preparing food" class="photo-warm" x="9" y="26" width="44" height="37"/>
    <rect role="img" aria-label="Photo of a team meeting around a table" class="photo-cool" x="66" y="26" width="44" height="37"/>
    <rect role="img" aria-label="Photo of colleagues shaking hands" x="124" y="26" width="44" height="37" fill="#c9ced4"/>
    <g class="sgd" font-size="2.2" text-anchor="middle"><text x="31" y="69">Service 1</text><text x="88" y="69">Service 2</text><text x="146" y="69">Service 3</text></g>
    <g class="b" font-size="1.6" text-anchor="middle"><text x="31" y="72.5">Reliability reviews and</text><text x="31" y="75">system health checks</text><text x="88" y="72.5">Cyber resiliency and</text><text x="88" y="75">business continuity</text><text x="146" y="72.5">Operational excellence</text><text x="146" y="75">and technical agility</text></g>
    <rect class="gold" y="92" width="176" height="7"/><circle cx="8" cy="95.5" r="1.4" fill="#fff" opacity=".7"/><text class="pg" x="167" y="96.3">PAGE | 06</text>
  </svg>
</div>

<div class="slide company" style="left:266px;top:190px">
  <svg viewBox="0 0 176 99">
    <text class="h hc" x="88" y="13">Our Company</text>
    <text class="b hc" x="88" y="17">A global partner for technical assurance.</text>
    <g class="b" text-anchor="middle"><text x="88" y="31">We help teams build systems that stay up, recover fast and scale with</text><text x="88" y="34">the business. Our consultants bring deep experience in fintech, pharma,</text><text x="88" y="37">retail and more, pairing careful analysis with practical delivery plans</text><text x="88" y="40">that leaders can trust from the first workshop to final hand over.</text></g>
    <rect class="gold" x="101" y="68" width="27" height="12"/>
    <g text-anchor="middle">
      <text class="num" x="18" y="73">2100</text><text class="b" x="18" y="77">Evaluations</text>
      <text class="num" x="60" y="73">3100</text><text class="b" x="60" y="77">Production profitably</text>
      <text x="114.5" y="73" fill="#fff" font-size="3.2" font-weight="700">2100</text><text class="bw" x="114.5" y="77">Companies</text>
      <text class="num" x="157" y="73">14</text><text class="b" x="157" y="77">Certifications</text>
    </g>
    <rect class="gold" y="92" width="176" height="7"/><circle cx="8" cy="95.5" r="1.4" fill="#fff" opacity=".7"/><text class="pg" x="167" y="96.3">PAGE | 07</text>
  </svg>
</div>

<div class="slide analysis" style="left:490px;top:190px">
  <svg viewBox="0 0 176 99">
    <text class="h hc" x="88" y="13">Analysis Chart</text>
    <text class="sgd" x="9" y="29">Bar Chart</text>
    <g stroke="#ddd" stroke-width=".2"><line x1="17" y1="39" x2="17" y2="73"/><line x1="31" y1="39" x2="31" y2="73"/><line x1="45" y1="39" x2="45" y2="73"/><line x1="59" y1="39" x2="59" y2="73"/><line x1="73" y1="39" x2="73" y2="73"/><line x1="87" y1="39" x2="87" y2="73"/></g>
    <g class="b" font-size="1.4"><text x="9" y="43">Category 1</text><text x="9" y="51">Category 2</text><text x="9" y="59">Category 3</text><text x="9" y="67">Category 4</text></g>
    <rect class="gold" x="17" y="41" width="20" height="2.5"/><rect class="char" x="37" y="41" width="12" height="2.5"/><rect class="grey" x="49" y="41" width="22" height="2.5"/>
    <rect class="gold" x="17" y="49" width="24" height="2.5"/><rect class="char" x="41" y="49" width="8" height="2.5"/><rect class="grey" x="49" y="49" width="5" height="2.5"/>
    <rect class="gold" x="17" y="57" width="16" height="2.5"/><rect class="char" x="33" y="57" width="18" height="2.5"/><rect class="grey" x="51" y="57" width="8" height="2.5"/>
    <rect class="gold" x="17" y="65" width="28" height="2.5"/><rect class="char" x="45" y="65" width="6" height="2.5"/><rect class="grey" x="51" y="65" width="12" height="2.5"/>
    <g class="sgd" font-size="2.2"><text x="94" y="30">Analysis 1</text><text x="94" y="50">Analysis 2</text><text x="94" y="70">Analysis 3</text></g>
    <g class="b" font-size="1.6"><text x="94" y="34">Uptime improved across core services in the last quarter.</text><text x="94" y="36.5">Incident count fell as monitoring and alerts were tuned.</text><text x="94" y="54">Recovery time dropped after runbooks were refreshed.</text><text x="94" y="56.5">Teams now rehearse failover drills on a fixed schedule.</text><text x="94" y="74">Change success rate rose with automated test gates.</text><text x="94" y="76.5">Costs held flat while capacity grew to meet demand.</text></g>
    <rect class="gold" y="92" width="176" height="7"/><circle cx="8" cy="95.5" r="1.4" fill="#fff" opacity=".7"/><text class="pg" x="167" y="96.3">PAGE | 08</text>
  </svg>
</div>

<div class="slide swot" style="left:717px;top:190px">
  <svg viewBox="0 0 176 99">
    <text class="h hc" x="88" y="12.5">S.W.O.T Analysis</text>
    <text class="h hc" x="88" y="18">Assumptions/Dependencies/Risks,</text>
    <g class="b" text-anchor="middle"><text x="88" y="25">We list each assumption, dependency and risk so that plans stay realistic</text><text x="88" y="27.5">and everyone knows what must hold true for the work to succeed.</text></g>
    <rect class="char" x="45" y="42" width="42" height="50"/><rect class="gold" x="129" y="42" width="47" height="50"/>
    <text class="sgd" x="9" y="47">Strength</text><text x="49" y="47" fill="#fff" font-size="2.4" font-weight="700">Weakness</text><text class="sgd" x="91" y="47">Opportunity</text><text x="133" y="47" fill="#fff" font-size="2.4" font-weight="700">Threat</text>
    <g class="b" font-size="1.6"><text x="9" y="52">1. Skilled senior team</text><text x="9" y="55">2. Proven methods</text><text x="9" y="58">3. Global reach</text><text x="9" y="61">4. Strong client trust</text>
      <text x="91" y="52">1. New cloud demand</text><text x="91" y="55">2. Stricter regulation</text><text x="91" y="58">3. Growing fintech market</text><text x="91" y="61">4. Partner channels</text></g>
    <g class="bw" font-size="1.6"><text x="49" y="52">1. Young brand</text><text x="49" y="55">2. Small bench</text><text x="49" y="58">3. Few case studies</text><text x="49" y="61">4. Limited tooling</text>
      <text x="133" y="52">1. Price pressure</text><text x="133" y="55">2. Talent shortage</text><text x="133" y="58">3. Vendor lock in</text><text x="133" y="61">4. Scope changes</text></g>
    <rect class="gold" y="92" width="176" height="7"/><circle cx="8" cy="95.5" r="1.4" fill="#fff" opacity=".7"/><text class="pg" x="167" y="96.3">PAGE | 09</text>
  </svg>
</div>

<div class="slide process" style="left:933px;top:190px">
  <svg viewBox="0 0 176 99">
    <rect role="img" aria-label="Photo of a young man working on a laptop" class="photo-cool" width="68" height="76"/>
    <text class="h" x="87" y="28">Process</text>
    <g class="b"><text x="87" y="34">A clear path from discovery to delivery, with checks</text><text x="87" y="36.5">at each stage to keep systems reliable and safe.</text></g>
    <g class="sg" stroke-width=".35" fill="none"><path d="M68 44 H86"/><path d="M68 56 H98"/><path d="M68 69 H108"/></g>
    <g class="gold"><path d="M86 43 L88 44 L86 45Z"/><path d="M98 55 L100 56 L98 57Z"/><path d="M108 68 L110 69 L108 70Z"/></g>
    <g class="sgd" font-size="2.3"><text x="87" y="45">Step 1</text><text x="100" y="57">Step 2</text><text x="111" y="70">Step 3</text></g>
    <g class="b" font-size="1.6"><text x="87" y="48.5">Discover current state and agree on shared goals.</text><text x="100" y="60.5">Design the target model and plan the key changes.</text><text x="111" y="73.5">Deliver, measure results and improve over time.</text></g>
    <rect class="gold" y="92" width="176" height="7"/><circle cx="8" cy="95.5" r="1.4" fill="#fff" opacity=".7"/><text class="pg" x="167" y="96.3">PAGE | 10</text>
  </svg>
</div>

<!-- Row 3 -->
<div class="slide planning" style="left:54px;top:313px">
  <svg viewBox="0 0 176 99">
    <rect role="img" aria-label="Photo of a modern house with a pool" x="9" y="22" width="73" height="66" fill="url(#cool)"/>
    <text class="h" x="87" y="28">Planning</text>
    <g class="b"><text x="87" y="33">Good plans turn goals into steps with owners, dates and</text><text x="87" y="35.5">clear checks, so progress is easy to follow and share.</text></g>
    <text class="sgd" x="87" y="44">Lorem ipsum do</text>
    <g class="b" font-size="1.6"><text x="89" y="47">• Map systems, owners and key risks</text><text x="89" y="49.5">• Set targets for uptime and recovery</text><text x="89" y="52">• Agree milestones with each team</text><text x="89" y="54.5">• Review progress every two weeks</text></g>
    <text class="sgd" x="87" y="61">Lorem ipsum do</text>
    <g class="b" font-size="1.6"><text x="89" y="64">• Track budget against planned scope</text><text x="89" y="66.5">• Log decisions and open questions</text><text x="89" y="69">• Share status with all stakeholders</text><text x="89" y="71.5">• Close each phase with a short review</text></g>
    <rect class="gold" y="92" width="176" height="7"/><circle cx="8" cy="95.5" r="1.4" fill="#fff" opacity=".7"/><text class="pg" x="167" y="96.3">PAGE | 11</text>
  </svg>
</div>

<div class="slide images" style="left:266px;top:313px">
  <svg viewBox="0 0 176 99">
    <rect role="img" aria-label="Photo of sparks from metal work" class="photo-warm" x="9" y="16" width="38" height="31"/>
    <rect role="img" aria-label="Photo of a woman working at a desk" class="photo-cool" x="84" y="16" width="38" height="31"/>
    <rect role="img" aria-label="Photo of hands holding a small house model" x="47" y="47" width="37" height="31" fill="#48586a"/>
    <text class="sgd" x="50" y="21">Item 2</text>
    <g class="b" font-size="1.6"><text x="50" y="24.5">Short notes on the work</text><text x="50" y="27">done in this phase and</text><text x="50" y="29.5">the value it created.</text></g>
    <text class="h" x="126" y="28" font-size="3.6">Images</text>
    <g class="b" font-size="1.6"><text x="126" y="32">Pictures from recent</text><text x="126" y="34.5">projects and client sites</text><text x="126" y="37">across several regions.</text></g>
    <text class="sgd" x="9" y="56">Item 1</text>
    <g class="b" font-size="1.6"><text x="9" y="59.5">Brief summary of the first</text><text x="9" y="62">item and its main result.</text></g>
    <text class="sgd" x="88" y="56">Item 3</text>
    <g class="b" font-size="1.6"><text x="88" y="59.5">Brief summary of the third</text><text x="88" y="62">item and its main result.</text></g>
    <rect class="gold" y="92" width="176" height="7"/><circle cx="8" cy="95.5" r="1.4" fill="#fff" opacity=".7"/><text class="pg" x="167" y="96.3">PAGE | 12</text>
  </svg>
</div>

<div class="slide leaders" style="left:490px;top:313px">
  <svg viewBox="0 0 176 99">
    <text class="h hc" x="88" y="13">Our Leaders</text>
    <text class="b hc" x="88" y="17">People who guide our work and our clients.</text>
    <rect class="gold" y="23" width="176" height="17"/>
    <g role="img" aria-label="Portraits of four leaders">
      <circle cx="26" cy="40" r="11" fill="#fff"/><circle cx="26" cy="40" r="10" fill="url(#warm)"/>
      <circle cx="69" cy="40" r="11" fill="#fff"/><circle cx="69" cy="40" r="10" fill="url(#warm)"/>
      <circle cx="112" cy="40" r="11" fill="#fff"/><circle cx="112" cy="40" r="10" fill="url(#warm)"/>
      <circle cx="151" cy="40" r="11" fill="#fff"/><circle cx="151" cy="40" r="10" fill="url(#cool)"/>
    </g>
    <g text-anchor="middle"><g class="sgd" font-size="2"><text x="26" y="56">Alex Moran</text><text x="69" y="56">Alex Moran</text><text x="112" y="56">Alex Moran</text><text x="151" y="56">Alex Moran</text></g>
    <g class="b" font-size="1.6"><text x="26" y="59">Manager</text><text x="69" y="59">Manager</text><text x="112" y="59">Manager</text><text x="151" y="59">Manager</text>
    <text x="26" y="63">Leads delivery for large</text><text x="26" y="65.5">assurance programmes.</text><text x="69" y="63">Leads delivery for large</text><text x="69" y="65.5">assurance programmes.</text><text x="112" y="63">Leads delivery for large</text><text x="112" y="65.5">assurance programmes.</text><text x="151" y="63">Leads delivery for large</text><text x="151" y="65.5">assurance programmes.</text></g></g>
    <rect class="gold" y="92" width="176" height="7"/><circle cx="8" cy="95.5" r="1.4" fill="#fff" opacity=".7"/><text class="pg" x="167" y="96.3">PAGE | 13</text>
  </svg>
</div>

<div class="slide team" style="left:717px;top:313px">
  <svg viewBox="0 0 176 99">
    <text class="h hc" x="88" y="13">Our Team</text>
    <text class="b hc" x="88" y="17">The people behind every engagement.</text>
    <rect class="char" x="141" y="19" width="35" height="38" rx="4"/>
    <g role="img" aria-label="Portraits of team members">
      <circle cx="30" cy="35" r="9.5" fill="url(#warm)"/><circle cx="73" cy="35" r="9.5" fill="url(#warm)"/><circle cx="116" cy="35" r="9.5" fill="url(#cool)"/><circle cx="156" cy="35" r="9.5" fill="url(#warm)" stroke="#fff" stroke-width=".8"/>
      <circle cx="30" cy="71" r="9.5" fill="url(#warm)"/><circle cx="73" cy="71" r="9.5" fill="url(#warm)"/><circle cx="116" cy="71" r="9.5" fill="url(#cool)"/><circle cx="156" cy="71" r="9.5" fill="url(#warm)"/>
    </g>
    <g text-anchor="middle" font-size="1.7">
      <g class="sgd" font-size="1.7"><text x="30" y="48">Alex Moran</text><text x="73" y="48">Alex Moran</text><text x="116" y="48">Alex Moran</text><text x="30" y="84">Alex Moran</text><text x="73" y="84">Alex Moran</text><text x="116" y="84">Alex Moran</text><text x="156" y="84">Alex Moran</text></g>
      <text x="156" y="50" fill="#fff" font-size="1.7" font-weight="700">Alex Moran</text><text x="156" y="52.5" fill="#fff" font-size="1.5">Manager</text>
      <g class="b" font-size="1.5"><text x="30" y="50.5">Manager</text><text x="73" y="50.5">Manager</text><text x="116" y="50.5">Manager</text><text x="30" y="86.5">Manager</text><text x="73" y="86.5">Manager</text><text x="116" y="86.5">Manager</text><text x="156" y="86.5">Manager</text></g>
    </g>
    <rect class="gold" y="92" width="176" height="7"/><circle cx="8" cy="95.5" r="1.4" fill="#fff" opacity=".7"/><text class="pg" x="167" y="96.3">PAGE | 14</text>
  </svg>
</div>

<div class="slide timeline" style="left:933px;top:313px">
  <svg viewBox="0 0 176 99">
    <text class="h hc" x="88" y="13">Timeline</text>
    <line x1="12" y1="49" x2="152" y2="49" stroke="#777" stroke-width=".3" stroke-dasharray="1 .8"/>
    <circle cx="12" cy="49" r=".8" class="grey"/><circle cx="152" cy="49" r=".8" class="grey"/>
    <g><circle cx="26" cy="49" r="3.2" class="gold"/><circle cx="49" cy="49" r="3.2" class="char"/><circle cx="71" cy="49" r="3.2" class="gold"/><circle cx="93" cy="49" r="3.2" class="char"/><circle cx="116" cy="49" r="3.2" class="gold"/><circle cx="138" cy="49" r="3.2" class="char"/></g>
    <g fill="#fff" font-size="1.4" text-anchor="middle" font-weight="700"><text x="26" y="49.6">2005</text><text x="49" y="49.6">2011</text><text x="71" y="49.6">2018</text><text x="93" y="49.6">2022</text><text x="116" y="49.6">2025</text><text x="138" y="49.6">2027</text></g>
    <g text-anchor="middle">
      <g class="s" font-size="2"><text x="49" y="24">Item 1</text><text x="93" y="24">Item 1</text><text x="138" y="24">Item 1</text></g>
      <g class="sgd" font-size="2"><text x="26" y="72">Item 1</text><text x="71" y="72">Item 1</text><text x="116" y="72">Item 1</text></g>
      <g class="b" font-size="1.5"><text x="49" y="27">Founded with a small team</text><text x="49" y="29">of senior engineers.</text><text x="93" y="27">Opened the first offices</text><text x="93" y="29">in Europe and Asia.</text><text x="138" y="27">Plan to double our</text><text x="138" y="29">client base worldwide.</text>
      <text x="26" y="75">First major client win</text><text x="26" y="77">in financial services.</text><text x="71" y="75">Launched a dedicated</text><text x="71" y="77">cyber resiliency unit.</text><text x="116" y="75">Expanded into pharma</text><text x="116" y="77">and retail sectors.</text></g>
    </g>
    <g fill="none" stroke-width=".4" class="sg"><circle cx="49" cy="19" r="1.3"/><circle cx="93" cy="19" r="1.3"/><circle cx="138" cy="19" r="1.3"/><circle cx="26" cy="67" r="1.3"/><circle cx="71" cy="67" r="1.3"/><circle cx="116" cy="67" r="1.3"/></g>
    <rect class="gold" y="92" width="176" height="7"/><circle cx="8" cy="95.5" r="1.4" fill="#fff" opacity=".7"/><text class="pg" x="167" y="96.3">PAGE | 15</text>
  </svg>
</div>

<!-- Row 4 -->
<div class="slide doughnut" style="left:54px;top:435px">
  <svg viewBox="0 0 176 99">
    <text class="h" x="8" y="28">Doughnut Chart</text>
    <g class="b"><text x="8" y="67">Quarterly share of completed</text><text x="8" y="69.5">assurance reviews across all</text><text x="8" y="72">regions and client groups.</text></g>
    <g fill="none" stroke-width="5.5" transform="rotate(-90 85 49)">
      <circle cx="85" cy="49" r="21" class="sg" stroke-dasharray="80 132" />
      <circle cx="85" cy="49" r="21" class="sc" stroke-dasharray="36 132" stroke-dashoffset="-80"/>
      <circle cx="85" cy="49" r="21" stroke="#8a8a8a" stroke-dasharray="8 132" stroke-dashoffset="-116"/>
      <circle cx="85" cy="49" r="21" stroke="#ccc" stroke-dasharray="8 132" stroke-dashoffset="-124"/>
    </g>
    <g class="b" font-size="1.5"><text x="66" y="78">● 1st Qtr  ● 2nd Qtr  ● 3rd Qtr  ● 4th Qtr</text></g>
    <text class="sgd" x="128" y="70" font-size="3">Total</text>
    <text class="num" x="128" y="77">13559</text>
    <rect class="gold" y="92" width="176" height="7"/><circle cx="8" cy="95.5" r="1.4" fill="#fff" opacity=".7"/><text class="pg" x="167" y="96.3">PAGE | 16</text>
  </svg>
</div>

<div class="slide info-one" style="left:266px;top:435px">
  <svg viewBox="0 0 176 99">
    <text class="h hc" x="88" y="13">infographic 01</text>
    <g stroke="#bbb" stroke-width=".3"><line x1="33" y1="40" x2="42" y2="40"/><line x1="66" y1="40" x2="76" y2="40"/><line x1="100" y1="40" x2="110" y2="40"/><line x1="134" y1="40" x2="143" y2="40"/></g>
    <g fill="#f3f3f3"><circle cx="23" cy="40" r="9.5"/><circle cx="56" cy="40" r="9.5"/><circle cx="122" cy="40" r="9.5"/><circle cx="155" cy="40" r="9.5"/></g>
    <polygon class="gold" points="89,30.5 97.5,35 97.5,45 89,49.5 80.5,45 80.5,35"/>
    <g text-anchor="middle" font-size="1.7" font-weight="600"><g class="sgd" font-size="1.7"><text x="23" y="40.6">Lorem ipsum</text><text x="56" y="40.6">Lorem ipsum</text><text x="122" y="40.6">Lorem ipsum</text><text x="155" y="40.6">Lorem ipsum</text></g><text x="89" y="40.6" fill="#fff">Lorem ipsum</text>
      <g class="sgd" font-size="1.8"><text x="23" y="56">Lorem ipsum</text><text x="56" y="56">Lorem ipsum</text><text x="89" y="56">Lorem ipsum</text><text x="122" y="56">Lorem ipsum</text><text x="155" y="56">Lorem ipsum</text></g>
      <g class="b" font-size="1.4" font-weight="400"><text x="23" y="59">Review current</text><text x="23" y="61">systems in depth</text><text x="56" y="59">Find the main</text><text x="56" y="61">gaps and risks</text><text x="89" y="59">Design the new</text><text x="89" y="61">target model</text><text x="122" y="59">Roll out change</text><text x="122" y="61">in small steps</text><text x="155" y="59">Measure and</text><text x="155" y="61">keep improving</text></g>
    </g>
    <rect class="gold" y="92" width="176" height="7"/><circle cx="8" cy="95.5" r="1.4" fill="#fff" opacity=".7"/><text class="pg" x="167" y="96.3">PAGE | 17</text>
  </svg>
</div>

<div class="slide info-two" style="left:490px;top:435px">
  <svg viewBox="0 0 176 99">
    <text class="h hc" x="88" y="13">infographic 02</text>
    <rect class="char" x="26" y="26" width="12" height="28" rx="6"/><rect class="gold" x="63" y="26" width="12" height="28" rx="6"/><rect class="char" x="100" y="26" width="12" height="28" rx="6"/><rect class="gold" x="136" y="26" width="12" height="28" rx="6"/>
    <g fill="#fff" font-size="1.6" font-weight="700" text-anchor="middle"><text x="32" y="38">Lorem</text><text x="32" y="40.5">Ipsum</text><text x="69" y="38">Lorem</text><text x="69" y="40.5">Ipsum</text><text x="106" y="38">Lorem</text><text x="106" y="40.5">Ipsum</text><text x="142" y="38">Lorem</text><text x="142" y="40.5">Ipsum</text></g>
    <g class="b" font-size="1.6" text-anchor="middle"><text x="32" y="60">Plan the review with</text><text x="32" y="62.5">each system owner.</text><text x="69" y="60">Test recovery paths</text><text x="69" y="62.5">under real load.</text><text x="106" y="60">Report findings with</text><text x="106" y="62.5">clear next steps.</text><text x="142" y="60">Secure key assets</text><text x="142" y="62.5">against new threats.</text></g>
    <g><polygon class="gold" points="32,67 36,69.3 36,73.7 32,76 28,73.7 28,69.3"/><polygon class="char" points="69,67 73,69.3 73,73.7 69,76 65,73.7 65,69.3"/><polygon class="gold" points="106,67 110,69.3 110,73.7 106,76 102,73.7 102,69.3"/><polygon class="char" points="142,67 146,69.3 146,73.7 142,76 138,73.7 138,69.3"/></g>
    <g fill="none" stroke="#fff" stroke-width=".35"><rect x="30.5" y="70.3" width="3" height="2.5"/><rect x="67.8" y="69.8" width="2.4" height="3.2"/><circle cx="106" cy="71.5" r="1.4"/><path d="M140.8 70 H143.2 V72 L142 73.2 L140.8 72Z"/></g>
    <rect class="gold" y="92" width="176" height="7"/><circle cx="8" cy="95.5" r="1.4" fill="#fff" opacity=".7"/><text class="pg" x="167" y="96.3">PAGE | 18</text>
  </svg>
</div>

<div class="slide info-three" style="left:717px;top:435px;background:var(--charcoal)">
  <svg viewBox="0 0 176 99">
    <text x="88" y="13" fill="#fff" font-size="4.4" font-weight="700" class="hc">infographic 03</text>
    <g class="gold"><path d="M12 34 H33 Q36 34 36 37 V74 Q36 80 30 80 H12Z"/><path d="M54 34 H75 Q78 34 78 37 V74 Q78 80 72 80 H54Z"/><path d="M96 34 H117 Q120 34 120 37 V74 Q120 80 114 80 H96Z"/><path d="M138 34 H159 Q162 34 162 37 V74 Q162 80 156 80 H138Z"/></g>
    <g fill="#fff" class="sc" stroke-width=".6"><circle cx="25" cy="40" r="9"/><circle cx="67" cy="40" r="9"/><circle cx="109" cy="40" r="9"/><circle cx="151" cy="40" r="9"/></g>
    <g class="num" font-size="5" text-anchor="middle"><text x="25" y="41">500</text><text x="67" y="41">600</text><text x="109" y="41">700</text><text x="151" y="41">800</text></g>
    <g class="sgd" font-size="1.5" text-anchor="middle"><text x="25" y="44">Point A</text><text x="67" y="44">Point B</text><text x="109" y="44">Point C</text><text x="151" y="44">Point D</text></g>
    <g fill="#fff" font-size="1.6" font-weight="700"><text x="13" y="56">Step One</text><text x="55" y="56">Step Two</text><text x="97" y="56">Step Three</text><text x="139" y="56">Step Four</text></g>
    <g class="bw" font-size="1.4"><text x="13" y="59">Short note on the</text><text x="13" y="61">first stage of work</text><text x="13" y="63">and its outcome.</text><text x="55" y="59">Short note on the</text><text x="55" y="61">second stage of</text><text x="55" y="63">work and results.</text><text x="97" y="59">Short note on the</text><text x="97" y="61">third stage of</text><text x="97" y="63">work and results.</text><text x="139" y="59">Short note on the</text><text x="139" y="61">final stage of</text><text x="139" y="63">work and results.</text></g>
    <rect class="gold" y="92" width="176" height="7"/><circle cx="8" cy="95.5" r="1.4" fill="#fff" opacity=".7"/><text class="pg" x="167" y="96.3">PAGE | 19</text>
  </svg>
</div>

<div class="slide agenda" style="left:933px;top:435px">
  <svg viewBox="0 0 176 99">
    <text class="h hc" x="88" y="13">Project Agenda</text>
    <text class="b hc" x="88" y="17">Key dates for the next stage of delivery.</text>
    <rect x="18" y="27" width="42" height="49" rx="2" fill="#f5f5f5"/><rect class="char" x="67" y="27" width="42" height="49" rx="2"/><rect x="116" y="27" width="42" height="49" rx="2" fill="#f5f5f5"/>
    <g fill="none" stroke-width=".5"><circle cx="39" cy="41" r="2.2" class="sg"/><rect x="85.5" y="38.5" width="5" height="4" rx=".6" stroke="#fff"/><circle cx="135.5" cy="40" r="1.2" class="sg"/><circle cx="139.5" cy="40" r="1.2" class="sg"/><path d="M133 44 Q135.5 41.5 138 44 M137 44 Q139.5 41.5 142 44" class="sg"/></g>
    <g text-anchor="middle" font-size="2.2" font-weight="700"><text class="sgd" x="39" y="52">23rd June</text><text x="88" y="52" fill="#fff">14th July</text><text class="sgd" x="137" y="52">01st December</text></g>
    <g font-size="1.5" text-anchor="middle"><g class="b" font-size="1.5"><text x="39" y="56">Kick off workshop with</text><text x="39" y="58.5">the client leadership and</text><text x="39" y="61">agree the review scope.</text><text x="137" y="56">Final report and road map</text><text x="137" y="58.5">shared with all teams for</text><text x="137" y="61">sign off and next steps.</text></g><g class="bw" font-size="1.5"><text x="88" y="56">Findings review with the</text><text x="88" y="58.5">technical owners and a</text><text x="88" y="61">draft plan for each gap.</text></g></g>
    <rect class="gold" y="92" width="176" height="7"/><circle cx="8" cy="95.5" r="1.4" fill="#fff" opacity=".7"/><text class="pg" x="167" y="96.3">PAGE | 20</text>
  </svg>
</div>

<!-- Row 5 -->
<div class="slide monthly" style="left:54px;top:569px">
  <svg viewBox="0 0 176 99">
    <text class="h hc" x="88" y="13">Monthly Chart</text>
    <text class="b hc" x="88" y="17">Monthly results for the core service line.</text>
    <g stroke="#e4e4e4" stroke-width=".2"><line x1="12" y1="28" x2="135" y2="28"/><line x1="12" y1="34" x2="135" y2="34"/><line x1="12" y1="40" x2="135" y2="40"/><line x1="12" y1="46" x2="135" y2="46"/><line x1="12" y1="52" x2="135" y2="52"/><line x1="12" y1="58" x2="135" y2="58"/><line x1="12" y1="64" x2="135" y2="64"/></g>
    <polyline points="20,37 38,48 56,42 74,37 92,44 110,30" fill="none" class="sg" stroke-width=".6"/>
    <g class="b" font-size="1.4"><text x="18" y="67">Jan</text><text x="36" y="67">Feb</text><text x="54" y="67">Mar</text><text x="72" y="67">Apr</text><text x="90" y="67">May</text><text x="108" y="67">Jun</text></g>
    <text class="sgd" x="133" y="29">May</text>
    <circle cx="137" cy="35" r="3.4" class="gold"/><text x="137" y="35.8" fill="#fff" font-size="2" font-weight="700" text-anchor="middle">3.5</text>
    <g class="b" font-size="1.5"><text x="133" y="41.5">Steady growth in new</text><text x="133" y="43.5">projects over the month.</text></g>
    <text class="sgd" x="133" y="54">June</text>
    <circle cx="137" cy="60" r="3.4" class="gold"/><text x="137" y="60.8" fill="#fff" font-size="2" font-weight="700" text-anchor="middle">5.7</text>
    <g class="b" font-size="1.5"><text x="133" y="66.5">Best month so far with</text><text x="133" y="68.5">strong client demand.</text></g>
    <rect class="gold" y="92" width="176" height="7"/><circle cx="8" cy="95.5" r="1.4" fill="#fff" opacity=".7"/><text class="pg" x="167" y="96.3">PAGE | 21</text>
  </svg>
</div>

<div class="slide three-point" style="left:266px;top:569px">
  <svg viewBox="0 0 176 99">
    <text class="h hc" x="88" y="13">Three Point Value</text>
    <text class="b hc" x="88" y="17">Three ways we add value for every client.</text>
    <g stroke="#7a7a7a" stroke-width="4" stroke-linecap="round"><line x1="18" y1="51" x2="41" y2="71"/><line x1="41" y1="71" x2="64" y2="42"/></g>
    <g class="gold" stroke="#7a7a7a" stroke-width=".8"><circle cx="18" cy="51" r="6"/><circle cx="41" cy="71" r="6"/><circle cx="64" cy="42" r="6"/></g>
    <g fill="#fff" font-size="3.4" font-weight="700" text-anchor="middle"><text x="18" y="52.2">1.</text><text x="41" y="72.2">2.</text><text x="64" y="43.2">3.</text></g>
    <g class="sgd" font-size="2.4"><text x="88" y="40">55%</text><text x="88" y="56">70%</text><text x="88" y="70">81%</text></g>
    <g class="b" font-size="1.6"><text x="88" y="43">Fewer incidents after our reliability reviews and</text><text x="88" y="45.3">better alerting across core production systems.</text><text x="88" y="59">Faster recovery times once runbooks and failover</text><text x="88" y="61.3">drills are in place for each critical service.</text><text x="88" y="73">Clients who extend their engagement after the</text><text x="88" y="75.3">first phase of assurance work is complete.</text></g>
    <rect class="gold" y="92" width="176" height="7"/><circle cx="8" cy="95.5" r="1.4" fill="#fff" opacity=".7"/><text class="pg" x="167" y="96.3">PAGE | 22</text>
  </svg>
</div>

<div class="slide table" style="left:490px;top:569px;background:var(--gold)">
  <svg viewBox="0 0 176 99">
    <text x="88" y="13" fill="#fff" font-size="4.4" font-weight="700" class="hc">Table</text>
    <text class="bw hc" x="88" y="17">Summary of products, profit and sales data.</text>
    <rect class="char" x="25" y="26" width="124" height="5"/>
    <rect class="char" x="25" y="42" width="124" height="11"/>
    <rect class="char" x="25" y="64" width="124" height="11"/>
    <g fill="#fff" font-size="1.8" font-weight="700"><text x="26" y="29.3">Data Name</text><text x="47" y="29.3">Product</text><text x="67" y="29.3">Profit</text><text x="88" y="29.3">Optional</text><text x="110" y="29.3">Sold</text><text x="129" y="29.3">Performance</text></g>
    <g fill="#fff" font-size="1.7">
      <text x="26" y="36">Data 1</text><text x="47" y="36">Product</text><text x="47" y="38.2">Name</text><text x="67" y="36">$900,000.00</text><text x="88" y="36">Yes</text><text x="110" y="36">70</text><text x="135" y="36">45%</text>
      <text x="26" y="46">Data 2</text><text x="47" y="46">Product</text><text x="47" y="48.2">Name</text><text x="67" y="46">$900,000.00</text><text x="88" y="46">No</text><text x="110" y="46">30</text><text x="135" y="46">20%</text>
      <text x="26" y="57">Data 3</text><text x="47" y="57">Product</text><text x="47" y="59.2">Name</text><text x="67" y="57">$900,000.00</text><text x="88" y="57">No</text><text x="110" y="57">20</text><text x="135" y="57">15%</text>
      <text x="26" y="68">Data 4</text><text x="47" y="68">Product</text><text x="47" y="70.2">Name</text><text x="67" y="68">$900,000.00</text><text x="88" y="68">Yes</text><text x="110" y="68">100</text><text x="135" y="68">60%</text>
      <text x="26" y="79">Data 5</text><text x="47" y="79">Product</text><text x="47" y="81.2">Name</text><text x="67" y="79">$900,000.00</text><text x="88" y="79">Yes</text><text x="110" y="79">50</text><text x="135" y="79">40%</text>
    </g>
    <circle cx="8" cy="95.5" r="1.4" fill="#fff" opacity=".7"/><text class="pg" x="167" y="96.3">PAGE | 23</text>
  </svg>
</div>

<div class="slide dash-one" style="left:717px;top:569px">
  <svg viewBox="0 0 176 99">
    <text class="h hc" x="88" y="13">Dashboard 01</text>
    <rect class="gold" x="100" y="25" width="25" height="11"/>
    <g text-anchor="middle"><g class="b" font-size="1.6"><text x="18" y="29">Customers</text><text x="59" y="29">Profitably</text><text x="157" y="29">Returns</text></g><text x="112.5" y="29" fill="#fff" font-size="1.6">Projects</text>
      <g class="num" font-size="2.3"><text x="18" y="33.5">2100</text><text x="59" y="33.5">3100</text><text x="157" y="33.5">14</text></g><text x="112.5" y="33.5" fill="#fff" font-size="2.3" font-weight="700">300</text></g>
    <g class="sgd" font-size="1.6"><text x="9" y="46">5 Active Users</text><text x="50" y="46">2 Users per sale</text></g>
    <g class="b" font-size="1.4"><text x="9" y="48.5">Last 10 Days</text><text x="50" y="48.5">Last 10 Days</text></g>
    <g><rect class="gold" x="15" y="62" width="12" height="1.6"/><rect class="char" x="27" y="62" width="9" height="1.6"/><rect class="grey" x="36" y="62" width="11" height="1.6"/>
    <rect class="gold" x="15" y="66" width="16" height="1.6"/><rect class="char" x="31" y="66" width="6" height="1.6"/>
    <rect class="gold" x="15" y="70" width="10" height="1.6"/><rect class="char" x="25" y="70" width="12" height="1.6"/><rect class="grey" x="37" y="70" width="5" height="1.6"/>
    <rect class="gold" x="15" y="74" width="18" height="1.6"/><rect class="char" x="33" y="74" width="4" height="1.6"/><rect class="grey" x="37" y="74" width="7" height="1.6"/></g>
    <g fill="none" stroke-width="2.5" transform="rotate(-90 88 67)"><circle cx="88" cy="67" r="7.5" class="sg" stroke-dasharray="34 47"/><circle cx="88" cy="67" r="7.5" class="sc" stroke-dasharray="13 47" stroke-dashoffset="-34"/></g>
    <text class="sgd" x="122" y="63" font-size="1.7">Live Profit &amp; Net Sales</text>
    <g fill="var(--gold)" font-size="1.6"><text x="122" y="67">Net Profit</text><text x="122" y="70.5" font-weight="700">$55.432M</text><text x="122" y="74">Sales = 400,000</text></g>
    <rect class="gold" y="92" width="176" height="7"/><circle cx="8" cy="95.5" r="1.4" fill="#fff" opacity=".7"/><text class="pg" x="167" y="96.3">PAGE | 24</text>
  </svg>
</div>

<div class="slide dash-two" style="left:933px;top:569px">
  <svg viewBox="0 0 176 99">
    <text class="h hc" x="88" y="13">Dashboard 02</text>
    <text class="b" x="9" y="26" font-size="1.4">Chart Title</text>
    <g stroke="#eee" stroke-width=".2"><line x1="14" y1="28" x2="98" y2="28"/><line x1="14" y1="36" x2="98" y2="36"/><line x1="14" y1="44" x2="98" y2="44"/><line x1="14" y1="52" x2="98" y2="52"/></g>
    <g class="gold"><rect x="17" y="29" width="2.6" height="25"/><rect x="27" y="29" width="2.6" height="25"/><rect x="37" y="29" width="2.6" height="25"/><rect x="47" y="29" width="2.6" height="25"/><rect x="57" y="29" width="2.6" height="25"/><rect x="67" y="29" width="2.6" height="25"/><rect x="77" y="29" width="2.6" height="25"/><rect x="87" y="29" width="2.6" height="25"/></g>
    <g transform="translate(140 41)"><path d="M0 0 L0 -8 A8 8 0 1 1 -5.5 5.8Z" class="gold"/><path d="M0 0 L-5.5 5.8 A8 8 0 0 1 -7.9 -1.2Z" class="char"/><path d="M0 0 L-7.9 -1.2 A8 8 0 0 1 -3.5 -7.2Z" class="grey"/><path d="M0 0 L-3.5 -7.2 A8 8 0 0 1 0 -8Z" fill="#ccc"/></g>
    <g>
      <path d="M10 83 V72 L16 68 L22 73 L27 70 V83Z" class="gold"/><path d="M10 83 L16 76 L22 79 L27 74 V83Z" class="char"/>
      <path d="M53 83 V73 L58 69 L63 71 L70 67 V83Z" class="gold"/><path d="M53 83 L58 77 L63 78 L70 73 V83Z" class="char"/>
      <path d="M95 83 V72 L101 69 L106 73 L112 71 V83Z" class="gold"/><path d="M95 83 L101 77 L106 79 L112 75 V83Z" class="char"/>
      <path d="M137 83 V72 L142 70 L148 72 L154 68 V83Z" class="gold"/><path d="M137 83 L142 78 L148 76 L154 74 V83Z" class="char"/>
    </g>
    <rect class="gold" y="92" width="176" height="7"/><circle cx="8" cy="95.5" r="1.4" fill="#fff" opacity=".7"/><text class="pg" x="167" y="96.3">PAGE | 25</text>
  </svg>
</div>

<!-- Row 6 -->
<div class="slide dash-three" style="left:54px;top:710px">
  <svg viewBox="0 0 176 99">
    <text class="h hc" x="88" y="13">Dashboard 03</text>
    <text class="b" x="43" y="19" font-size="1.6">Chart Title</text>
    <g stroke="#eee" stroke-width=".2"><line x1="10" y1="22" x2="80" y2="22"/><line x1="10" y1="27" x2="80" y2="27"/><line x1="10" y1="32" x2="80" y2="32"/><line x1="10" y1="37" x2="80" y2="37"/></g>
    <polyline points="14,28 26,31 40,23 52,30 64,26 76,33" fill="none" class="sc" stroke-width=".4"/>
    <polyline points="14,33 26,26 40,30 52,25 64,29 76,27" fill="none" class="sg" stroke-width=".4"/>
    <polyline points="14,30 26,33 40,34 52,32 64,33 76,31" fill="none" stroke="#aaa" stroke-width=".4"/>
    <text class="b" x="125" y="22" font-size="1.6">Chart Title</text>
    <g><rect class="gold" x="108" y="26" width="14" height="1.4"/><rect class="char" x="122" y="26" width="8" height="1.4"/><rect class="gold" x="108" y="30" width="20" height="1.4"/><rect class="char" x="128" y="30" width="6" height="1.4"/><rect class="gold" x="108" y="34" width="18" height="1.4"/><rect class="char" x="126" y="34" width="12" height="1.4"/><rect class="gold" x="108" y="38" width="22" height="1.4"/><rect class="char" x="130" y="38" width="9" height="1.4"/></g>
    <text class="b" x="43" y="51" font-size="1.6">Chart Title</text>
    <g><rect class="grey" x="12" y="66" width="2" height="14"/><rect class="char" x="14.5" y="71" width="2" height="9"/><rect class="gold" x="17" y="69" width="2" height="11"/>
      <rect class="grey" x="30" y="62" width="2" height="18"/><rect class="char" x="32.5" y="69" width="2" height="11"/><rect class="gold" x="35" y="72" width="2" height="8"/>
      <rect class="grey" x="48" y="66" width="2" height="14"/><rect class="char" x="50.5" y="73" width="2" height="7"/><rect class="gold" x="53" y="68" width="2" height="12"/>
      <rect class="grey" x="66" y="70" width="2" height="10"/><rect class="char" x="68.5" y="66" width="2" height="14"/><rect class="gold" x="71" y="61" width="2" height="19"/></g>
    <line x1="10" y1="80" x2="80" y2="80" stroke="#ccc" stroke-width=".2"/>
    <circle cx="103" cy="68" r="3.6" class="gold"/><rect x="101.8" y="66.5" width="2.4" height="3" fill="none" stroke="#fff" stroke-width=".35"/>
    <text class="num" x="109" y="69.5" font-size="3.6">436.00</text>
    <g class="b" font-size="1.5"><text x="101" y="74.5">Total hours logged on client</text><text x="101" y="76.5">assurance work this quarter.</text></g>
    <rect class="gold" y="92" width="176" height="7"/><circle cx="8" cy="95.5" r="1.4" fill="#fff" opacity=".7"/><text class="pg" x="167" y="96.3">PAGE | 26</text>
  </svg>
</div>

<div class="slide dash-four" style="left:266px;top:710px">
  <svg viewBox="0 0 176 99">
    <text class="h hc" x="88" y="13">Dashboard 04</text>
    <text class="b" x="58" y="19" font-size="1.6">Chart Title</text>
    <path d="M13 27 L50 26 L90 27 L113 33 L127 26 V55 H13Z" class="grey"/>
    <path d="M13 38 L50 36 L90 37 L113 44 L127 36 V55 H13Z" class="gold"/>
    <g class="b" font-size="1.3"><text x="13" y="58">2020</text><text x="50" y="58">2021</text><text x="90" y="58">2022</text><text x="120" y="58">2023</text></g>
    <rect class="light" x="129" y="23" width="16" height="7"/><rect class="light" x="129" y="33" width="16" height="7"/><rect class="gold" x="129" y="43" width="16" height="7"/>
    <g font-size="1.5"><text class="sgd" x="130.5" y="26" font-size="1.5">120</text><text class="b" x="130.5" y="28.3" font-size="1.5">Sales</text><text class="sgd" x="130.5" y="36" font-size="1.5">40</text><text class="b" x="130.5" y="38.3" font-size="1.5">New Clients</text><text x="130.5" y="46" fill="#fff" font-size="1.5">14</text><text x="130.5" y="48.3" fill="#fff" font-size="1.5">Employees</text></g>
    <text class="b" x="58" y="66" font-size="1.6">Chart Title</text>
    <g><rect class="gold" x="18" y="69" width="34" height="1.4"/><rect class="char" x="52" y="69" width="22" height="1.4"/><rect class="grey" x="74" y="69" width="25" height="1.4"/>
    <rect class="gold" x="18" y="73" width="40" height="1.4"/><rect class="char" x="58" y="73" width="26" height="1.4"/><rect class="grey" x="84" y="73" width="15" height="1.4"/>
    <rect class="gold" x="18" y="77" width="28" height="1.4"/><rect class="char" x="46" y="77" width="30" height="1.4"/><rect class="grey" x="76" y="77" width="23" height="1.4"/>
    <rect class="gold" x="18" y="81" width="44" height="1.4"/><rect class="char" x="62" y="81" width="20" height="1.4"/><rect class="grey" x="82" y="81" width="17" height="1.4"/></g>
    <text class="sgd" x="129" y="68" font-size="1.8">Title</text>
    <g class="b" font-size="1.4"><text x="129" y="71">Sales held steady while new</text><text x="129" y="73">clients grew each quarter,</text><text x="129" y="75">led by strong demand in</text><text x="129" y="77">fintech and retail sectors.</text></g>
    <rect class="gold" y="92" width="176" height="7"/><circle cx="8" cy="95.5" r="1.4" fill="#fff" opacity=".7"/><text class="pg" x="167" y="96.3">PAGE | 27</text>
  </svg>
</div>

<div class="slide thanks" style="left:490px;top:710px;background:var(--gold)">
  <svg viewBox="0 0 176 99">
    <text x="88" y="35" fill="#fff" font-size="9" class="hc">THANK YOU</text>
    <line x1="84" y1="39" x2="92" y2="39" stroke="#fff" stroke-width=".3"/>
    <g class="bw" font-size="2" text-anchor="middle"><text x="88" y="44">Thank you for your time. We look forward to building reliable, resilient</text><text x="88" y="47">systems with your team and to the next steps of our work together on</text><text x="88" y="50">this programme. Reach us any time at veltrano dot biz.</text></g>
    <circle cx="8" cy="95.5" r="1.4" fill="#fff" opacity=".7"/>
  </svg>
</div>

<div class="slide icons" style="left:717px;top:710px">
  <svg viewBox="0 0 176 99" fill="none" stroke="var(--gold)" stroke-width=".5" role="img" aria-label="Set of simple business icons">
    <circle cx="22" cy="15" r="2.5"/><rect x="53" y="12.5" width="4" height="5"/><circle cx="88" cy="15" r="2.8"/><path d="M86 15 H90 M88 12.2 V17.8"/><circle cx="122" cy="14" r="1.8"/><rect x="151" y="13" width="5" height="4" rx=".5"/>
    <circle cx="22" cy="32" r="2.5"/><path d="M22 30.5 V32 L23 33"/><path d="M53 30 L57 34 M57 30 L53 34"/><rect x="86" y="30.5" width="4.5" height="3.2" rx=".4"/><circle cx="122" cy="32" r="2"/><path d="M151 31 L155 30 V34 L151 33Z"/>
    <circle cx="22" cy="48" r="2.5"/><path d="M53.5 49.5 L55 46 L56.5 49.5"/><circle cx="88" cy="47" r="1.3"/><path d="M85.5 50 Q88 47.5 90.5 50"/><path d="M120 46 Q122 44 124 46 L123 50 H121Z"/><path d="M151 48 H157 M152 46.5 L156 46.5"/>
    <path d="M20 67 V64 M22 67 V62 M24 67 V60"/><rect x="53" y="61" width="4" height="5.5"/><path d="M86 61 H90 V64 L88 66.5 L86 64Z"/><circle cx="121" cy="63" r="1.1"/><circle cx="124" cy="63" r="1.1"/><path d="M119 66.5 Q122.5 63.5 126 66.5"/><circle cx="154" cy="64" r="2.4"/><circle cx="154" cy="64" r=".8"/>
    <path d="M20 79 H23 V84 H20Z"/><polygon points="55,78 57.5,79.5 57.5,82.5 55,84 52.5,82.5 52.5,79.5"/><path d="M88 78 A2 2 0 0 1 90 80 C90 82 88 84 88 84 C88 84 86 82 86 80 A2 2 0 0 1 88 78Z"/><rect x="119.5" y="79" width="5" height="3.6"/><path d="M119.5 79 L122 81 L124.5 79"/><circle cx="154" cy="79.5" r="1.3"/><path d="M151.5 84 Q154 81 156.5 84"/>
    <rect y="92" width="176" height="7" fill="var(--gold)" stroke="none"/><text class="pg" x="167" y="96.3" stroke="none">PAGE | 29</text>
  </svg>
</div>

</body>
</html>
```